依頼概要
■依頼の目的/概要
5月~販売する居酒屋のPOPのデザインをお願いします。

■依頼詳細
メニューブック・又は看板に告知用として貼り付けます。

■重視する点
ジンギスカンは臭いイメージがあるので、そこを覆す
『他店とは違う商品』『専門業者』がわかるようなPOPを
Illustrator・Photoshopの経験必須でお願いします。
お客様の目線に立ったデザインをしていただきたいのです。

その他何かご不明な点がございましたら、お気軽にご質問下さい。
よろしくお願いいたします。
店舗の ロゴを追加します。

店名『松葉亭 別館』
松葉亭別館 ロゴデータ追加
出来てますか??
■ 選んだ理由

スッキリと告知!をメインに打ち出していただき、共感できました。

■ 提案者全員のお礼・コメント

定期的に制作があるので、お願いしたいです。

```html
<!DOCTYPE html>
<html lang="ja">
<head>
<meta charset="UTF-8">
<title>松葉亭別館 ジンギスカン 夏季限定</title>
<link href="https://fonts.googleapis.com/css2?family=Shippori+Mincho+B1:wght@800&family=M+PLUS+1p:wght@800;900&family=Dela+Gothic+One&display=swap" rel="stylesheet">
<style>
  :root {
    --ink: #111111;
    --red: #d7141a;
    --yellow: #ffe14a;
    --white: #ffffff;
    --night: #050505;
    --meat-dark: #3a2418;
    --meat-mid: #7a5440;
    --meat-light: #b08868;
  }
  * { margin: 0; padding: 0; box-sizing: border-box; }
  html, body { width: 849px; height: 1200px; overflow: hidden; background: var(--white); }
  .poster {
    position: relative; width: 849px; height: 1200px; overflow: hidden;
    background: var(--night);
    font-family: "M PLUS 1p", sans-serif;
  }
  .header {
    position: absolute; left: 0; top: 0; width: 100%; height: 215px;
    background: var(--white);
  }
  .headline {
    position: absolute; left: 130px; top: 22px;
    font-family: "Shippori Mincho B1", serif; font-weight: 800;
    font-size: 38px; line-height: 1.3; color: var(--ink);
    white-space: nowrap;
  }
  .headline .accent { color: var(--red); }
  .store-name {
    position: absolute; right: 34px; top: 28px;
    font-family: "Shippori Mincho B1", serif; font-weight: 800;
    font-size: 30px; color: var(--ink); letter-spacing: 2px;
  }
  .dish-photo {
    position: absolute; left: 0; top: 200px; width: 100%; height: 650px;
    background: radial-gradient(ellipse 60% 45% at 50% 45%, var(--meat-light) 0%, var(--meat-mid) 40%, var(--meat-dark) 75%, var(--night) 100%);
  }
  .photo-fade {
    position: absolute; left: 0; top: 720px; width: 100%; height: 140px;
    background: linear-gradient(to bottom, rgba(5,5,5,0), var(--night));
  }
  .invite-card {
    position: absolute; left: 195px; top: 340px;
    padding: 12px 18px; background: rgba(255,255,255,0.9);
    transform: rotate(-8deg); white-space: nowrap;
    font-family: "Shippori Mincho B1", serif; font-weight: 800;
    font-size: 20px; line-height: 1.5; color: var(--red);
  }
  .season-note {
    position: absolute; left: 115px; top: 660px;
    font-family: "Shippori Mincho B1", serif; font-weight: 800;
    font-size: 34px; line-height: 1.35; color: var(--yellow);
    text-shadow: 0 0 8px #000, 0 0 3px #000; white-space: nowrap;
  }
  .reserve-badge {
    position: absolute; left: 592px; top: 660px; width: 140px; height: 140px;
    border-radius: 50%; background: var(--red); border: 4px solid var(--white);
    display: flex; flex-direction: column; align-items: center; justify-content: center;
    color: var(--white); font-weight: 900; line-height: 1.2;
  }
  .reserve-badge .small { font-size: 22px; color: var(--yellow); }
  .reserve-badge .large { font-size: 32px; }
  .title-rule { position: absolute; left: 60px; width: 729px; height: 2px; background: var(--white); }
  .title-rule.top { top: 838px; }
  .title-rule.bottom { top: 975px; }
  .title {
    position: absolute; left: 0; top: 830px; width: 100%;
    text-align: center; color: var(--white);
    font-weight: 900; font-size: 110px; line-height: 1.3; letter-spacing: 4px;
  }
  .tag {
    position: absolute; top: 995px; height: 115px; background: var(--red); color: var(--white);
    font-weight: 900; text-align: center;
  }
  .tag.courses { left: 60px; width: 82px; padding-top: 10px; }
  .tag.courses .unit-top { font-size: 24px; display: block; line-height: 1.2; }
  .tag.courses .num { font-size: 52px; line-height: 1; }
  .tag.courses .unit { font-size: 24px; }
  .tag.drinks { left: 155px; width: 110px; padding-top: 8px; }
  .tag.drinks .num { font-size: 48px; line-height: 1.05; display: block; }
  .tag.drinks .note { font-size: 16px; line-height: 1.2; display: block; }
  .price {
    position: absolute; left: 295px; top: 1005px;
    font-family: "Dela Gothic One", sans-serif; color: var(--red);
    font-size: 104px; line-height: 1; letter-spacing: -2px;
    white-space: nowrap; transform: skewX(-8deg);
  }
  .price .yen { font-size: 72px; }
  .price .tax {
    position: absolute; right: -6px; top: -24px;
    font-family: "M PLUS 1p", sans-serif; font-weight: 800;
    font-size: 22px; color: var(--white); letter-spacing: 0;
  }
  .extra-note {
    position: absolute; left: 60px; top: 1130px;
    color: var(--white); font-size: 16px; font-weight: 800;
  }
</style>
</head>
<body>
<main class="poster">
  <div class="dish-photo" role="img" aria-label="鉄鍋で焼かれるジンギスカンの羊肉と野菜を箸で持ち上げる写真"></div>
  <div class="photo-fade"></div>

  <header class="header">
    <h1 class="headline">
      専門業者だから出せる、<br>
      <span class="accent">「臭みのない」</span>絶品の味。<br>
      ジンギスカンの常識を超えた!!
    </h1>
    <div class="store-name">松葉亭別館</div>
  </header>

  <p class="invite-card">今まで「ジンギスカンは苦手」<br>という方にも召し上がって欲しい味!<br>ご予約お待ちしております!</p>

  <p class="season-note">『5月~8月夏季限定』<br>松葉亭の夏の定番</p>

  <div class="reserve-badge"><span class="small">先行予約</span><span class="large">受付中</span></div>

  <div class="title-rule top"></div>
  <h2 class="title">ジンギスカン</h2>
  <div class="title-rule bottom"></div>

  <div class="tag courses"><span class="unit-top">全</span><span class="num">6</span><span class="unit">品</span></div>
  <div class="tag drinks"><span class="num">3</span><span class="note">時間<br>飲み放題付</span></div>

  <div class="price">3,480<span class="yen">円</span><span class="tax">+税</span></div>

  <p class="extra-note">食べ放題はプラス500円(+税)</p>
</main>
</body>
</html>
```